Ward Compass Business Card Design*

We need a business card design for our company Ward Compass. Our company is specialized in providing online consulting services regarding medical institutions, hospitals and doctors. We work with patients worldwide looking to choose between healthcare providers. We have a website you may use as a reference, where we list doctors and clinics worldwide. So we target Medical providers as well as patients worldwide.
Target Market(s)
Medical Providers and patients around the world
Industry/Entity Type
Medical
Contact Information for Business Card
Salma Derkaoui
CEO
+90 612 348 2071
info@wardcompass-example.com
www.wardcompass-example.com
14 Annakhil 3 H.R.B. Rabat, Morocco
Requirements
Must have
- Company logo/name on one full side, personal info and smaller logo and company name on the other side.
Nice to have
- Smart and elegant design

```html
<!DOCTYPE html>
<html lang="en">
<head>
<meta charset="utf-8">
<title>Ward Compass Business Card</title>
<link rel="stylesheet" href="https://fonts.googleapis.com/css2?family=Open+Sans:wght@400;600;700&display=swap">
<style>
  :root {
    --navy: #1d3f6b;
    --navy-deep: #173457;
    --ink: #2a2a2a;
    --grey: #6f6f6f;
    --pale: #e4e9f0;
    --paper: #ffffff;
    --backdrop: #dcdcdc;
  }
  * { box-sizing: border-box; margin: 0; padding: 0; }
  html, body {
    width: 1200px; height: 768px; overflow: hidden;
    background: var(--backdrop);
    font-family: "Open Sans", Arial, sans-serif;
  }
  .sheet {
    width: 1200px; height: 768px;
    display: flex; align-items: center; justify-content: center; gap: 40px;
  }
  .card {
    position: relative;
    width: 540px; height: 308px;
    overflow: hidden;
    box-shadow: 0 6px 18px rgba(0,0,0,.18);
  }
  /* Back side */
  .card--back { background: var(--navy); color: var(--paper); }
  .back-brand {
    position: absolute; left: 0; right: 0; top: 112px;
    display: flex; align-items: center; justify-content: center; gap: 14px;
  }
  .back-brand .dot {
    width: 22px; height: 22px; border-radius: 50%; background: var(--paper);
  }
  .back-brand .name {
    font-weight: 600; font-size: 30px; letter-spacing: 1px; color: var(--paper);
  }
  .back-web {
    position: absolute; left: 0; right: 0; bottom: 40px; text-align: center;
    font-size: 13px; letter-spacing: 6px; color: var(--paper);
  }
  /* Front side */
  .card--front { background: var(--paper); color: var(--ink); }
  .front-mark {
    position: absolute; right: -70px; bottom: -120px;
    width: 330px; height: 330px; border-radius: 50%; background: var(--pale);
  }
  .front-brand {
    position: absolute; left: 36px; top: 34px;
    display: flex; align-items: center; gap: 10px;
  }
  .front-brand .dot { width: 16px; height: 16px; border-radius: 50%; background: var(--navy); }
  .front-brand .name {
    font-weight: 700; font-size: 19px; letter-spacing: 1.5px;
    text-transform: uppercase; color: var(--navy);
  }
  .contact {
    position: absolute; left: 36px; top: 140px;
    font-size: 13.5px; line-height: 20px; color: var(--ink);
    list-style: none;
  }
  .contact li { display: flex; align-items: center; gap: 8px; }
  .contact .address { padding-left: 20px; }
  .contact svg { width: 12px; height: 12px; fill: var(--navy); flex: none; }
  .person {
    position: absolute; right: 34px; bottom: 56px; text-align: right;
  }
  .person .fullname { font-weight: 700; font-size: 23px; color: var(--navy); }
  .person .role { font-size: 15px; color: var(--grey); letter-spacing: .5px; }
</style>
</head>
<body>
<main class="sheet">
  <section class="card card--back" aria-label="Card back">
    <div class="back-brand">
      <span class="dot"></span>
      <span class="name">Ward Compass</span>
    </div>
    <p class="back-web">www.wardcompass-example.com</p>
  </section>

  <section class="card card--front" aria-label="Card front">
    <div class="front-mark"></div>
    <div class="front-brand">
      <span class="dot"></span>
      <span class="name">Ward Compass</span>
    </div>
    <ul class="contact">
      <li class="address">14 Annakhil 3</li>
      <li class="address">H.R.B. Rabat, Morocco</li>
      <li>
        <svg viewBox="0 0 12 12"><path d="M2.5 1h2l1 3-1.5 1a7 7 0 0 0 3 3l1-1.5 3 1v2a1 1 0 0 1-1 1A10 10 0 0 1 1.5 2a1 1 0 0 1 1-1z"/></svg>
        +90 612 348 2071
      </li>
      <li>
        <svg viewBox="0 0 12 12"><path d="M0 2h12v1L6 7 0 3zM0 4.5l6 4 6-4V10H0z"/></svg>
        info@wardcompass-example.com
      </li>
      <li>
        <svg viewBox="0 0 12 12"><circle cx="6" cy="6" r="6"/><path d="M1 6h10M6 0.5v11" stroke="#fff" stroke-width="1"/></svg>
        www.wardcompass-example.com
      </li>
    </ul>
    <div class="person">
      <p class="fullname">Salma Derkaoui</p>
      <p class="role">CEO</p>
    </div>
  </section>
</main>
</body>
</html>
```